Holiday Ornament Design for guest giveaway

We are looking for art for a two sided ornament to gift to clients to celebrate the holidays (The actual size of the ornament measures 2 1/4 inch all round but we always have to provide artwork with bleed which would be about an eighth of an inch extra all around). Side one: "peace on earth" in the style of attached inspiration picture, and side two: the cherub in a complementing style

Industry/Entity Type

Hospitality

Colors
0094D4
00A9DD
6FCCEA
C7EBF8
E9F6FB

Requirements
Must have
• clarity, incorporate year "2023" somewhere in design either cherub side or peace on earth side.
Nice to have
• Design style of the peace on earth image, foliage in planet style with wording clearly inside

```html
<!DOCTYPE html>
<html lang="en">
<head>
<meta charset="utf-8">
<title>Holiday Ornament – Peace on Earth / 2023</title>
<link rel="stylesheet" href="https://fonts.googleapis.com/css2?family=Kaushan+Script&family=Montserrat:wght@500;800&family=Dancing+Script:wght@500&display=swap">
<style>
  :root {
    --backdrop: #9a5c5e;
    --ornament-base: #f4fbfb;
    --wreath-teal: #9fcfcb;
    --wreath-pale: #dff1ef;
    --wreath-red: #d8283a;
    --ink-red: #d41f35;
    --ink-red-light: #e9474f;
    --ink-slate: #5f7f7c;
    --ink-navy: #1f3150;
    --cherub-line: #b3222e;
  }
  html, body {
    margin: 0;
    padding: 0;
    width: 1200px;
    height: 765px;
    overflow: hidden;
    background: var(--backdrop);
  }
  .canvas {
    position: relative;
    width: 1200px;
    height: 765px;
  }
  .ornament {
    position: absolute;
    width: 532px;
    height: 532px;
    top: 108px;
  }
  .ornament--front { left: 58px; }
  .ornament--back  { left: 628px; }
  .ornament svg { display: block; width: 100%; height: 100%; }
  .arc-greeting {
    font-family: "Montserrat", sans-serif;
    font-weight: 500;
    font-size: 15px;
    letter-spacing: 5px;
    fill: var(--ink-navy);
  }
  .arc-signoff-script {
    font-family: "Dancing Script", cursive;
    font-size: 15px;
    letter-spacing: 3px;
  }
  .arc-heart { fill: var(--ink-navy); }
  .headline {
    font-family: "Kaushan Script", cursive;
  }
  .headline--peace { font-size: 104px; fill: var(--ink-red); }
  .headline--on    { font-size: 54px;  fill: var(--ink-red-light); }
  .headline--earth { font-size: 96px;  fill: var(--ink-slate); }
  .year-mark {
    font-family: "Montserrat", sans-serif;
    font-weight: 800;
    font-size: 46px;
    letter-spacing: 9px;
    fill: var(--ink-red);
  }
</style>
</head>
<body>
<main class="canvas">

  <!-- Side one: Peace on Earth -->
  <section class="ornament ornament--front" aria-label="Ornament side one">
    <svg viewBox="0 0 532 532">
      <defs>
        <radialGradient id="wreathTone" cx="266" cy="266" r="250" gradientUnits="userSpaceOnUse">
          <stop offset="0.5" stop-color="var(--wreath-pale)"/>
          <stop offset="0.62" stop-color="var(--wreath-teal)"/>
          <stop offset="0.74" stop-color="var(--wreath-red)" stop-opacity="0.75"/>
          <stop offset="0.86" stop-color="var(--wreath-teal)"/>
          <stop offset="0.96" stop-color="var(--wreath-pale)"/>
        </radialGradient>
        <path id="arcTop" d="M 38,266 A 228,228 0 0 1 494,266"/>
        <path id="arcBottom" d="M 20,266 A 246,246 0 0 0 512,266"/>
      </defs>

      <circle class="ornament-face" cx="266" cy="266" r="266" fill="var(--ornament-base)"/>

      <circle class="wreath" role="img" aria-label="Illustrated evergreen wreath with red and white baubles, bows, gifts and stars"
              cx="266" cy="266" r="180" fill="none" stroke="url(#wreathTone)" stroke-width="88"/>

      <text class="arc-greeting">
        <textPath href="#arcTop" startOffset="50%" text-anchor="middle">MERRY CHRISTMAS</textPath>
      </text>
      <text class="arc-greeting">
        <textPath href="#arcBottom" startOffset="50%" text-anchor="middle"><tspan class="arc-signoff-script">with love</tspan><tspan class="arc-heart"> ♥ </tspan>THE HARTWELLS</textPath>
      </text>

      <text class="headline headline--peace" x="262" y="246" text-anchor="middle">Peace</text>
      <text class="headline headline--on" x="304" y="285" text-anchor="middle">on</text>
      <text class="headline headline--earth" x="276" y="352" text-anchor="middle">Earth</text>
    </svg>
  </section>

  <!-- Side two: Cherub -->
  <section class="ornament ornament--back" aria-label="Ornament side two">
    <svg viewBox="0 0 532 532">
      <defs>
        <radialGradient id="festiveField" cx="266" cy="266" r="266" gradientUnits="userSpaceOnUse">
          <stop offset="0.35" stop-color="#ffffff"/>
          <stop offset="0.62" stop-color="var(--wreath-pale)"/>
          <stop offset="0.8" stop-color="var(--wreath-teal)"/>
          <stop offset="0.92" stop-color="#e59aa0"/>
          <stop offset="1" stop-color="var(--wreath-teal)"/>
        </radialGradient>
        <clipPath id="faceClip"><circle cx="266" cy="266" r="266"/></clipPath>
      </defs>

      <g clip-path="url(#faceClip)">
        <rect class="festive-field" role="img" aria-label="Dense pattern of evergreen boughs, red baubles, gifts and stars"
              x="0" y="0" width="532" height="532" fill="url(#festiveField)"/>
      </g>

      <ellipse class="cherub-figure" role="img" aria-label="Red line drawing of a cherub crowned with grape leaves, drinking from a raised cup"
               cx="272" cy="290" rx="128" ry="198" fill="#ffffff" fill-opacity="0.9"
               stroke="var(--cherub-line)" stroke-width="2"/>

      <text class="year-mark" x="270" y="66" text-anchor="middle">2023</text>
    </svg>
  </section>

</main>
</body>
</html>
```